Bramwell Joinery Website

My client Bramwell Joinery is looking for a redesign for a Word Press Website. Their current site is at www.bramwelljoinery.example They are a custom cabinet company, but also create bathroom, living room, bar and entertainment and bedroom cabinets too. They would like a design that emulates the master craftsman work they do yet a contemporary style.

Their current site was designed using Flash elements.

Target Market(s)

Home owners and builders of high end homes

Industry/Entity Type

Entertainment

Font styles to use
Serif
Decorative

Requirements
Must have
• Must show their work and logo using a contemporary style.
Nice to have
• Sliders that showcase their projects.

```html
<!DOCTYPE html>
<html lang="en">
<head>
<meta charset="utf-8">
<title>Bramwell Joinery</title>
<link rel="stylesheet" href="https://fonts.googleapis.com/css2?family=Noto+Serif:ital,wght@0,400;0,700;1,400&family=Raleway:wght@500;700&display=swap">
<style>
:root{
  --wood-dark:#2a190e;
  --wood-mid:#4a2f1a;
  --wood-light:#5e3d22;
  --green:#4fe04a;
  --ink:#4a4a4a;
  --muted:#6b6b6b;
  --line:#c9c9c9;
  --white:#ffffff;
}
*{margin:0;padding:0;box-sizing:border-box}
html,body{width:949px;height:1200px;overflow:hidden;background:var(--white)}
body{position:relative;font-family:"Noto Serif",serif;color:var(--ink)}
.abs{position:absolute}
.wood{background:repeating-linear-gradient(90deg,var(--wood-dark) 0 18px,var(--wood-mid) 18px 40px,var(--wood-light) 40px 52px,var(--wood-mid) 52px 70px)}
.header{left:0;top:0;width:949px;height:130px}
.brand{left:89px;top:17px;width:120px;height:94px;display:flex;align-items:center;gap:8px}
.brand-dot{width:22px;height:22px;border-radius:50%;background:var(--green);flex:none}
.brand-name{color:var(--white);font-size:17px;font-weight:700;line-height:1.15}
.util{top:13px;font-family:"Raleway",sans-serif;font-size:11px;color:var(--white);font-weight:500}
.phone-btn{left:736px;top:0;width:124px;height:31px;background:var(--green);color:var(--white);font-family:"Raleway",sans-serif;font-weight:700;font-size:14px;display:flex;align-items:center;justify-content:center;gap:7px}
.nav{top:62px;font-size:15px;color:var(--white)}
.nav-rule{left:243px;top:95px;width:616px;height:1px;background:rgba(255,255,255,.45)}
.nav-active{left:250px;top:93px;width:53px;height:4px;border-radius:2px;background:var(--green)}
.hero{left:0;top:130px;width:949px;height:502px;background:linear-gradient(180deg,#e9ddc8 0%,#b0502c 30%,#7a2c14 60%,#c9b79e 100%)}
.caption{left:87px;top:283px;width:433px;height:154px;background:rgba(30,20,14,.62);padding:14px 12px}
.caption h1{font-weight:400;font-size:36px;color:var(--white);line-height:1.1;letter-spacing:.5px}
.caption p{margin-top:10px;font-size:14.5px;line-height:20px;color:var(--white)}
.dot{top:569px;width:8px;height:8px;border-radius:50%;background:var(--white)}
.dot.on{background:var(--green);box-shadow:0 0 0 2px var(--white)}
.card{top:675px;width:177px;height:148px;border:1px solid #aaa;padding:3px}
.card-img{width:100%;height:100%;position:relative}
.card-label{position:absolute;left:0;bottom:0;width:100%;height:34px;background:#111;color:var(--white);font-size:14.5px;display:flex;align-items:center;justify-content:center}
.intro{left:89px;top:860px;width:570px;font-style:italic;font-size:13px;line-height:20px;color:var(--muted)}
.badge{background:#b5b5b5;border-radius:3px}
.band{left:0;top:952px;width:949px;height:73px}
.foot-brand{left:89px;top:1055px;display:flex;align-items:center;gap:6px;color:#3fb83a;font-size:12px;font-weight:700;line-height:1.2}
.foot-brand .brand-dot{width:14px;height:14px;background:#3fb83a}
.contact{left:197px;font-size:12px;display:flex;align-items:center;gap:10px;color:var(--ink)}
.contact svg{width:11px;height:11px;fill:#999}
.foot-nav{right:92px;top:1057px;font-size:12px;color:var(--ink);white-space:nowrap}
.foot-nav .sep{margin:0 6px;color:#666}
.foot-row{right:92px;top:1095px;font-size:12px;display:flex;align-items:center;gap:12px;color:var(--ink)}
.social{width:14px;height:14px;border-radius:50%;background:#222}
.bottom{left:0;top:1158px;width:949px;height:42px;display:flex;align-items:center;justify-content:center;color:var(--white);font-size:12px}
</style>
</head>
<body>

<header class="abs header wood">
  <div class="abs brand"><span class="brand-dot"></span><span class="brand-name">Bramwell Joinery</span></div>
  <span class="abs util" style="left:482px">Who We Are</span>
  <span class="abs util" style="left:566px">Getting Started</span>
  <span class="abs util" style="left:660px">Contact Us</span>
  <div class="abs phone-btn">
    <svg width="12" height="14" viewBox="0 0 24 24" fill="#fff"><path d="M6.6 10.8a15 15 0 0 0 6.6 6.6l2.2-2.2c.3-.3.7-.4 1-.2 1.1.4 2.3.6 3.6.6.6 0 1 .4 1 1V20c0 .6-.4 1-1 1A17 17 0 0 1 3 4c0-.6.4-1 1-1h3.5c.6 0 1 .4 1 1 0 1.3.2 2.5.6 3.6.1.3 0 .7-.2 1z"/></svg>
    555 010 234
  </div>
  <span class="abs nav" style="left:259px">Home</span>
  <span class="abs nav" style="left:355px">Customer Experience</span>
  <span class="abs nav" style="left:530px">Professional</span>
  <span class="abs nav" style="left:643px">Portfolio</span>
  <span class="abs nav" style="left:732px">Cabinet Hardware</span>
  <div class="abs nav-rule"></div>
  <div class="abs nav-active"></div>
</header>

<section class="abs hero" role="img" aria-label="Photo of a kitchen with rich cherry wood cabinets and a central island"></section>
<div class="abs caption">
  <h1>Welcome To Bramwell</h1>
  <p>Lorem ipsum dolor sit amet, consectetur adipiscing elit, sed do eiusmod tempor incididunt ut labore et dolore magna al iqua. Ut enim ad minim veniam, quis nostrud</p>
</div>
<span class="abs dot" style="left:457px"></span>
<span class="abs dot on" style="left:470px"></span>
<span class="abs dot" style="left:483px"></span>

<div class="abs card" style="left:90px"><div class="card-img" role="img" aria-label="Photo of a carved wooden door" style="background:linear-gradient(90deg,#3a2214,#6a3f22,#3a2214)"><span class="card-label">SHOP DOOR STYLE</span></div></div>
<div class="abs card" style="left:288px"><div class="card-img" role="img" aria-label="Photo of a white kitchen with pendant lights" style="background:linear-gradient(180deg,#3a2c22,#d8d0c4 50%,#2a2420)"><span class="card-label">CITCHEN GALLERY</span></div></div>
<div class="abs card" style="left:484px"><div class="card-img" role="img" aria-label="Photo of a black custom kitchen island" style="background:linear-gradient(180deg,#d9d4c8,#1e1e22 55%)"><span class="card-label">CUSTOM DESIGN</span></div></div>
<div class="abs card" style="left:679px"><div class="card-img" role="img" aria-label="Photo of a quote form on a green clipboard" style="background:linear-gradient(160deg,#c9c4bc,#f2f2ee 50%,#bfe07a)"><span class="card-label">GET QUICK QUOTE</span></div></div>

<p class="abs intro">Sed ut perspiciatis unde omnis iste natus error sit voluptatem accusantium doloremque lau­dantium, totam rem aperiam, eaque ipsa quae ab illo inventore veritatis et quasi architecto beatae vitae dicta sunt explicabo. Nemo enim ipsam voluptatem quia voluptas sit aspernatur</p>
<div class="abs badge" style="left:714px;top:866px;width:42px;height:22px"></div>
<div class="abs badge" style="left:714px;top:894px;width:42px;height:20px"></div>
<div class="abs badge" style="left:763px;top:866px;width:40px;height:22px"></div>
<div class="abs badge" style="left:763px;top:897px;width:42px;height:16px"></div>
<div class="abs badge" style="left:810px;top:870px;width:46px;height:42px"></div>

<div class="abs band wood"></div>

<footer>
  <div class="abs foot-brand"><span class="brand-dot"></span><span>Bramwell<br>Joinery</span></div>
  <div class="abs contact" style="top:1057px"><svg viewBox="0 0 24 24"><path d="M12 2a7 7 0 0 0-7 7c0 5 7 13 7 13s7-8 7-13a7 7 0 0 0-7-7zm0 9.5A2.5 2.5 0 1 1 12 6.5a2.5 2.5 0 0 1 0 5z"/></svg>ABC Building, 123 Office, Street, Lorem Ipsum.</div>
  <div class="abs contact" style="top:1078px;font-weight:700"><svg viewBox="0 0 24 24"><path d="M6.6 10.8a15 15 0 0 0 6.6 6.6l2.2-2.2c.3-.3.7-.4 1-.2 1.1.4 2.3.6 3.6.6.6 0 1 .4 1 1V20c0 .6-.4 1-1 1A17 17 0 0 1 3 4c0-.6.4-1 1-1h3.5c.6 0 1 .4 1 1 0 1.3.2 2.5.6 3.6.1.3 0 .7-.2 1z"/></svg>555 010 234</div>
  <div class="abs contact" style="top:1099px"><svg viewBox="0 0 24 24"><path d="M2 5h20v14H2zm2 2v.5l8 5 8-5V7z"/></svg>info@bramwelljoinery.example</div>

  <div class="abs foot-nav">Home<span class="sep">/</span> Customer Experience<span class="sep">/</span> Professional<span class="sep">/</span> Contact Us</div>
  <div class="abs foot-row">
    <span class="social"></span><span class="social"></span><span class="social"></span>
    <span>|</span><span>Terms of use</span><span>|</span><span>Privacy Policy</span>
  </div>

  <div class="abs bottom wood">© 2015 Bramwell Joinery</div>
</footer>

</body>
</html>
```